Corvenne Jewelers Business Cards

A creative, cool edgy business card for our entire team that says we are a young, hip, luxury jewelry store specializing in diamonds and engagement rings but that we are also personal shoppers and trusted advisors. Our colors are Navy Blue & Platinum

I have included our past business card.

Font styles to use
Serif

Colors
0255a3

Requirements
Nice to have
• A card stock that you can write on with a pen

```html
<!DOCTYPE html>
<html lang="en">
<head>
<meta charset="utf-8">
<title>Corvenne Jewelers Business Cards</title>
<link href="https://fonts.googleapis.com/css2?family=Playfair+Display+SC:wght@700&family=Source+Serif+4:wght@400;600&display=swap" rel="stylesheet">
<style>
  :root {
    --navy: #1f2266;
    --navy-soft: #3a3d80;
    --ornament-strong: rgba(31, 34, 102, 0.55);
    --ornament-mid: rgba(31, 34, 102, 0.32);
    --ornament-light: rgba(31, 34, 102, 0.12);
    --card: #fbfbfd;
    --stage: #e4e6ee;
  }
  * { margin: 0; padding: 0; box-sizing: border-box; }
  html, body { width: 1200px; height: 800px; overflow: hidden; }
  body {
    background: var(--stage);
    font-family: "Source Serif 4", Georgia, serif;
    color: var(--navy);
    position: relative;
  }
  .card {
    position: absolute;
    top: 250px;
    width: 525px;
    height: 300px;
    background: var(--card);
    border-radius: 22px;
    overflow: hidden;
    box-shadow: 0 6px 20px rgba(31, 34, 102, 0.14);
  }
  .card--back { left: 50px; }
  .card--front { left: 625px; }

  .ornament {
    position: absolute;
    background: linear-gradient(120deg, var(--ornament-mid) 0%, var(--ornament-strong) 35%, var(--ornament-light) 70%, var(--ornament-mid) 100%);
  }
  .corner {
    width: 90px;
    height: 90px;
    border-radius: 50%;
    background: radial-gradient(circle, var(--ornament-strong) 0%, var(--ornament-mid) 55%, var(--ornament-light) 100%);
  }

  /* back side */
  .back-vine {
    left: 18px;
    top: 40px;
    width: 150px;
    height: 250px;
    border-radius: 75px;
  }
  .back-corner-tl { left: 150px; top: -45px; }
  .back-corner-br { right: -45px; bottom: 70px; }
  .brand {
    position: absolute;
    left: 215px;
    top: 112px;
  }
  .brand-name {
    display: flex;
    align-items: center;
    gap: 10px;
    font-size: 22px;
    font-weight: 400;
    letter-spacing: 0.04em;
    color: var(--navy);
  }
  .brand-name .dot { width: 9px; height: 9px; border-radius: 50%; background: var(--navy); }
  .brand-web { margin-top: 8px; padding-left: 19px; font-size: 11px; letter-spacing: 0.08em; color: var(--navy-soft); }

  /* front side */
  .front-vine-top {
    left: 30px;
    top: 14px;
    width: 465px;
    height: 74px;
    border-radius: 37px;
  }
  .front-vine-right {
    right: 18px;
    top: 60px;
    width: 40px;
    height: 80px;
    border-radius: 20px;
  }
  .front-vine-bottom {
    left: 40px;
    top: 216px;
    width: 400px;
    height: 58px;
    border-radius: 29px;
  }
  .front-corner-bl { left: -40px; bottom: -40px; }
  .front-corner-br { right: -40px; bottom: -40px; }
  .role {
    position: absolute;
    top: 100px;
    left: 0;
    width: 100%;
    text-align: center;
  }
  .role-title {
    font-family: "Playfair Display SC", Georgia, serif;
    font-size: 26px;
    font-weight: 700;
    letter-spacing: 0.03em;
    line-height: 1;
  }
  .role-sub { font-size: 12px; letter-spacing: 0.18em; text-transform: uppercase; margin-top: 4px; }
  .contacts {
    position: absolute;
    top: 158px;
    left: 28px;
    right: 28px;
    display: flex;
    justify-content: space-between;
    font-size: 10px;
    line-height: 1.5;
    letter-spacing: 0.03em;
  }
  .contact { display: flex; gap: 7px; align-items: flex-start; }
  .contact svg { flex: none; fill: var(--navy); }
  .caps { text-transform: uppercase; }
  .rule {
    position: absolute;
    left: 28px;
    right: 28px;
    top: 203px;
    height: 2px;
    background: var(--navy);
  }
</style>
</head>
<body>
  <section class="card card--back" aria-label="Card back">
    <div class="ornament back-vine" role="img" aria-label="Navy floral vine ornament with flowers and leaves"></div>
    <div class="ornament corner back-corner-tl" role="img" aria-label="Navy corner fan ornament"></div>
    <div class="ornament corner back-corner-br" role="img" aria-label="Navy corner fan ornament"></div>
    <div class="brand">
      <div class="brand-name"><span class="dot"></span>Corvenne Jewelers</div>
      <div class="brand-web">www.corvennejewelers.com</div>
    </div>
  </section>

  <section class="card card--front" aria-label="Card front">
    <div class="ornament front-vine-top" role="img" aria-label="Navy floral vine ornament across the top"></div>
    <div class="ornament front-vine-right" role="img" aria-label="Navy tulip bud ornament"></div>
    <div class="ornament front-vine-bottom" role="img" aria-label="Navy floral border ornament"></div>
    <div class="ornament corner front-corner-bl" role="img" aria-label="Navy corner fan ornament"></div>
    <div class="ornament corner front-corner-br" role="img" aria-label="Navy corner fan ornament"></div>

    <div class="role">
      <div class="role-title">Partner</div>
      <div class="role-sub">Marketing Director</div>
    </div>

    <div class="contacts">
      <div class="contact">
        <svg width="11" height="15" viewBox="0 0 12 16" aria-hidden="true"><path d="M6 0a6 6 0 0 0-6 6c0 4.5 6 10 6 10s6-5.5 6-10a6 6 0 0 0-6-6zm0 8.3A2.3 2.3 0 1 1 6 3.7a2.3 2.3 0 0 1 0 4.6z"/></svg>
        <div class="caps">24 Wexley Lane<br>Ashmoor, Connecticut 06099</div>
      </div>
      <div class="contact">
        <svg width="14" height="14" viewBox="0 0 16 16" aria-hidden="true"><path d="M3.5 1 6 3.8 4.7 5.6a9 9 0 0 0 5.7 5.7L12.2 10 15 12.5 13.4 15C7 15 1 9 1 2.6z"/></svg>
        <div>C (555) 014-2290<br>O (555) 014-7735</div>
      </div>
      <div class="contact">
        <svg width="16" height="12" viewBox="0 0 16 12" aria-hidden="true"><path d="M0 0h16v12H0z M1 1.2v.6l7 5 7-5v-.6z" fill-rule="evenodd"/></svg>
        <div>Lenora@corvennejewelers.com</div>
      </div>
    </div>
    <div class="rule"></div>
  </section>
</body>
</html>
```